Velmaro App for Smart Devices IoT WiFi Electronic

Velmaro is a siren manufacturer. This application is used for the company's products that have a Wi-Fi connection and an internet connection, which can be configured and activated remotely through this application. In addition, this application is used to activate the siren at specific times for the start and end of shifts in companies and schools. Users will be siren installers and IT or HR managers.
In addition to activating motorized sirens timers, some siren models have speakers and allow you to play TTS (text to speech) audio, audio recorded by the user on the phone and upload audio (mp3) with playlist programming with start and end times.
Application screens: home with dashboard (one dashboard for each category). Device categories: timers, speakers, motorized siren. Screen for requesting evaluation in the Play Store. Screen for registering the user profile. Screen for registering devices according to their category (timers, speakers, motorized siren). Screen for registering device groups. Screen for pairing the device on the client's Wi-Fi network. Screen for registering activation times. Screen for uploading MP3 audios. Screen for registering playlists with audio selection, start and end times. Screen for recording audio for later sending to the speakers. Screen for converting text to speech and sending to the speakers. It is important to have a time picker with the day of the week to program the activation times and playlist.

Target Market(s)

Schools, Companies and Stores.

Industry/Entity Type

IoT

Font styles to use
Sans Serif
Other font styles liked:
• roboto

Colors
FFC000
F8CF3A
FAE287
FDF2CF
FEFAEE

Requirements
Must have
• time picker with weekdays for timer programming feature.
Nice to have
• app review request screen on play store

```html
<!DOCTYPE html>
<html lang="en">
<head>
<meta charset="utf-8">
<title>Velmaro – Timers</title>
<link rel="stylesheet" href="https://fonts.googleapis.com/css2?family=Roboto:wght@400;500;700&display=swap">
<style>
  :root{
    --primary:#F2BF00;
    --primary-soft:#F8CF3A;
    --primary-pale:#FDF2CF;
    --page:#FEFAEE;
    --status-bar:#9E7F1F;
    --ink:#1C1C1C;
    --ink-muted:#5E5E5E;
    --placeholder:#6E6E6E;
    --line:#ECECEC;
    --field-border:#E6E6E6;
    --off:#D6D6D6;
    --off-text:#BDBDBD;
    --white:#FFFFFF;
  }
  *{box-sizing:border-box;margin:0;padding:0}
  html,body{width:1200px;height:2181px;overflow:hidden;background:var(--page);font-family:"Roboto",Arial,sans-serif;color:var(--ink)}
  .screen{position:absolute;left:100px;top:0;width:1000px;height:2181px;background:var(--status-bar);overflow:hidden}
  .status-bar{position:absolute;left:0;top:0;width:100%;height:128px;color:var(--white)}
  .status-time{position:absolute;left:56px;top:26px;font-size:36px;font-weight:500;letter-spacing:1px}
  .status-icons{position:absolute;right:50px;top:32px;display:flex;gap:14px;align-items:center}
  .sheet{position:absolute;left:0;top:128px;width:100%;height:2053px;background:var(--white);border-radius:56px 56px 0 0}
  .abs{position:absolute}
  .handle{left:452px;top:22px;width:96px;height:9px;border-radius:5px;background:var(--primary)}
  .sheet-title{left:0;width:100%;top:80px;text-align:center;font-size:48px;font-weight:700;line-height:56px}
  .close-btn{right:58px;top:44px;width:52px;height:52px}
  .section-title{left:56px;font-size:40px;font-weight:700;line-height:48px}
  .field{border:2px solid var(--field-border);border-radius:20px;height:104px;display:flex;align-items:center;padding-left:32px;font-size:30px}
  .field.device{left:56px;top:271px;width:888px;font-weight:500}
  .field.date{top:609px;width:431px;font-size:27px;color:var(--placeholder)}
  .field-label{font-size:32px;font-weight:500;line-height:40px;top:560px}
  .option{left:56px;width:888px}
  .option-title{font-size:37px;font-weight:500;line-height:44px}
  .option-desc{font-size:27px;color:var(--ink-muted);margin-top:20px;line-height:32px}
  .divider{left:56px;width:888px;height:2px;background:var(--line)}
  .toggle{right:56px;width:122px;height:69px;border-radius:35px;background:var(--off)}
  .toggle::after{content:"";position:absolute;left:5px;top:5px;width:59px;height:59px;border-radius:50%;background:var(--white);box-shadow:0 2px 4px rgba(0,0,0,.18)}
  .toggle.on{background:var(--primary)}
  .toggle.on::after{left:58px}
  .weekday{top:1655px;width:100px;margin-left:-50px;text-align:center;color:var(--primary)}
  .weekday .dot{width:52px;height:52px;margin:0 auto;border:3px solid var(--primary);border-radius:50%;display:flex;align-items:center;justify-content:center;font-size:30px;font-weight:500;background:var(--page)}
  .weekday .name{font-size:21px;font-weight:500;margin-top:8px}
  .weekday.off{color:var(--off-text)}
  .weekday.off .dot{border-color:var(--off-text);background:var(--white)}
  .period{top:1810px;display:flex;align-items:center;gap:14px;font-size:32px;color:var(--off-text)}
  .radio{width:28px;height:28px;border-radius:50%;border:2px solid var(--off)}
  .period.active{color:var(--primary-soft)}
  .period.active .radio{border:none;background:radial-gradient(circle,var(--primary) 0 6px,var(--primary-pale) 7px 14px)}
  .save-btn{left:50px;top:1894px;width:900px;height:112px;border-radius:26px;background:var(--primary);color:var(--white);font-size:34px;font-weight:500;display:flex;align-items:center;justify-content:center;border:none;font-family:inherit}
</style>
</head>
<body>
<main class="screen">
  <header class="status-bar">
    <span class="status-time">09:41</span>
    <div class="status-icons">
      <svg width="40" height="26" viewBox="0 0 40 26"><rect x="0" y="18" width="7" height="8" rx="1.5" fill="#fff"/><rect x="10" y="13" width="7" height="13" rx="1.5" fill="#fff"/><rect x="20" y="7" width="7" height="19" rx="1.5" fill="#fff"/><rect x="30" y="0" width="7" height="26" rx="1.5" fill="#fff" opacity=".4"/></svg>
      <svg width="36" height="26" viewBox="0 0 36 26"><path d="M18 26l-5-6a7 7 0 0 1 10 0z" fill="#fff"/><path d="M8 14a14 14 0 0 1 20 0l-3 3a10 10 0 0 0-14 0z" fill="#fff"/><path d="M2 8a22 22 0 0 1 32 0l-3 3a18 18 0 0 0-26 0z" fill="#fff"/></svg>
      <svg width="52" height="26" viewBox="0 0 52 26"><rect x="1" y="1" width="44" height="24" rx="6" fill="none" stroke="#fff" stroke-width="2" opacity=".5"/><rect x="4" y="4" width="38" height="18" rx="4" fill="#fff"/><rect x="47" y="9" width="4" height="8" rx="2" fill="#fff" opacity=".5"/></svg>
    </div>
  </header>

  <section class="sheet">
    <div class="abs handle"></div>
    <h1 class="abs sheet-title">Timers</h1>
    <svg class="abs close-btn" viewBox="0 0 52 52" aria-label="Close"><path d="M8 8L44 44M44 8L8 44" stroke="var(--primary)" stroke-width="5" stroke-linecap="round"/></svg>

    <h2 class="abs section-title" style="top:183px">Select Device</h2>
    <div class="abs field device">Gate A</div>

    <h2 class="abs section-title" style="top:462px">Select Date &amp; Time</h2>
    <span class="abs field-label" style="left:56px">Start Date</span>
    <span class="abs field-label" style="left:524px">End Date</span>
    <div class="abs field date" style="left:56px">Select Date</div>
    <div class="abs field date" style="left:513px">Select Date</div>

    <h2 class="abs section-title" style="top:819px">Repeat</h2>

    <div class="abs option" style="top:950px"><p class="option-title">One Time</p><p class="option-desc">It will happen once and then it will be closed.</p></div>
    <div class="abs toggle" style="top:1000px"></div>
    <div class="abs divider" style="top:1095px"></div>

    <div class="abs option" style="top:1135px"><p class="option-title">Daily</p><p class="option-desc">On a daily basis, according to the time you have set.</p></div>
    <div class="abs toggle" style="top:1183px"></div>
    <div class="abs divider" style="top:1273px"></div>

    <div class="abs option" style="top:1313px"><p class="option-title">Weekly</p><p class="option-desc">On a weekly basis, according to the time you have set.</p></div>
    <div class="abs toggle" style="top:1361px"></div>
    <div class="abs divider" style="top:1459px"></div>

    <div class="abs option" style="top:1499px"><p class="option-title">Custom</p><p class="option-desc">In which you can set the day according to your preference.</p></div>
    <div class="abs toggle on" style="top:1546px"></div>

    <div class="abs weekday" style="left:96px"><div class="dot">M</div><div class="name">MON</div></div>
    <div class="abs weekday" style="left:229px"><div class="dot">T</div><div class="name">TUE</div></div>
    <div class="abs weekday" style="left:362px"><div class="dot">W</div><div class="name">WED</div></div>
    <div class="abs weekday" style="left:500px"><div class="dot">T</div><div class="name">THU</div></div>
    <div class="abs weekday" style="left:638px"><div class="dot">F</div><div class="name">FRI</div></div>
    <div class="abs weekday off" style="left:777px"><div class="dot">S</div><div class="name">SAT</div></div>
    <div class="abs weekday off" style="left:912px"><div class="dot">S</div><div class="name">SUN</div></div>

    <div class="abs period" style="left:62px"><span class="radio"></span>Once</div>
    <div class="abs period active" style="left:260px"><span class="radio"></span>Month</div>
    <div class="abs period" style="left:473px"><span class="radio"></span>Year</div>

    <button class="abs save-btn" type="button">Save</button>
  </section>
</main>
</body>
</html>
```